Redesign for Popular UK Town Website

We're looking for someone to redesign a website for a popular tourist town that's visited by over 250,000 people a year. We have a basic design frame in place and need someone to make it look more 'professional.'
We've created a temporary design layout to show you a general idea of what we're looking for: http://dorrin.co.uk/
All text/images are placeholder images so you can get an idea of the general layout.
(Please note that you can grab any images found on the internet for 'tenby' to be used as placeholder images. This is because we will be visiting the locations and taking our own photos, after the design is complete.)
Target Market(s)
Tourists
Industry/Entity Type
Town
Number of Pages Required
2 page
Requirements
Must have
- You need to redesign the homepage: http://dorrin.co.uk/
- You also need to redesign the following page: http://dorrin.co.uk/hotels/ (This page will be used for multiple categories and is used to list locations of properties/places etc.)
- Design must be responsive also.
Nice to have
- Please feel free to add as much as you can to the content/features as with our limited knowledge of websites, have only been able to create a basic layout.

```html
<!DOCTYPE html>
<html lang="en">
<head>
<meta charset="utf-8">
<title>Hotels in Dorrin</title>
<link rel="stylesheet" href="https://fonts.googleapis.com/css2?family=Roboto:wght@300;400;500;700&display=swap">
<style>
:root{
  --blue:#0aa3e0;
  --blue-dark:#0a8cc4;
  --navy:#0f2a44;
  --navy-deep:#0a1f33;
  --ink:#333;
  --muted:#777;
  --line:#e3e3e3;
  --white:#fff;
}
*{box-sizing:border-box;margin:0;padding:0}
html,body{width:811px;height:1200px;overflow:hidden}
body{font-family:'Roboto',sans-serif;color:var(--ink);background:var(--white);position:relative}
.site-header{height:32px;display:flex;align-items:center;justify-content:space-between;padding:0 28px;background:var(--white);box-shadow:0 1px 3px rgba(0,0,0,.08);position:relative;z-index:2}
.brand{display:flex;align-items:center;gap:5px;font-weight:700;font-size:13px;color:var(--navy)}
.brand-dot{width:12px;height:12px;border-radius:50%;background:var(--blue)}
.main-nav{display:flex;gap:14px;font-size:8px;color:var(--ink)}
.main-nav .active{color:var(--blue)}
.page-hero{height:118px;background:var(--blue);color:var(--white);text-align:center;padding-top:36px}
.page-hero h1{font-size:20px;font-weight:500}
.breadcrumb{font-size:7px;margin-top:5px;opacity:.9}
.listing{width:640px;margin:0 auto;padding-top:38px;text-align:center}
.listing h2{font-size:19px;font-weight:400;color:#222}
.intro{font-size:7.5px;line-height:1.6;color:var(--muted);width:400px;margin:12px auto 22px}
.card-grid{display:grid;grid-template-columns:repeat(3,1fr);gap:14px 14px;text-align:left}
.card{border:1px solid var(--line);background:var(--white);height:280px}
.card-photo{height:180px}
.card-body{padding:12px 10px}
.card-body h3{font-size:9px;font-weight:500;margin-bottom:7px;color:#222}
.detail{display:flex;align-items:center;gap:4px;font-size:6.5px;color:var(--muted);margin-bottom:4px}
.detail svg{width:7px;height:7px;fill:var(--blue);flex:none}
.detail b{font-weight:500;color:var(--ink)}
.load-more{display:inline-block;margin-top:26px;padding:6px 16px;border:1px solid var(--blue);color:var(--blue);font-size:7px;border-radius:2px}
.site-footer{position:absolute;left:0;top:965px;width:811px;height:210px;background:linear-gradient(160deg,#1a3a58,var(--navy) 55%,#0c2238);color:#cfd8e2;display:flex;padding:30px 0 0 70px}
.footer-brand{width:250px;display:flex;flex-direction:column;align-items:center;gap:8px;padding-top:20px}
.footer-brand .mark{width:46px;height:46px;border-radius:50%;border:2px solid var(--white)}
.footer-brand span{font-size:20px;font-weight:700;color:var(--white)}
.footer-col{width:170px}
.footer-col h4{font-size:9px;font-weight:500;color:var(--white);margin-bottom:8px}
.footer-col li{list-style:none;font-size:7px;margin-bottom:6px;padding-left:8px;position:relative}
.footer-col li::before{content:"";position:absolute;left:0;top:2px;width:3px;height:3px;border-top:1px solid var(--blue);border-right:1px solid var(--blue);transform:rotate(45deg)}
.updates{width:170px;background:rgba(255,255,255,.06);padding:6px;font-size:6px;line-height:1.5}
.updates .feed-title{color:var(--white);margin-bottom:6px}
.tweet{display:flex;gap:5px;margin-bottom:9px}
.avatar{width:14px;height:14px;border-radius:50%;background:#5b7a96;flex:none}
.copyright{position:absolute;left:0;top:1175px;width:811px;height:25px;background:var(--navy-deep);color:#8fa2b5;font-size:6px;display:flex;align-items:center;justify-content:center;gap:6px}
.copyright strong{color:var(--white);font-weight:700}
.to-top{position:absolute;right:14px;top:1148px;width:18px;height:18px;border-radius:50%;background:var(--blue);display:flex;align-items:center;justify-content:center}
</style>
</head>
<body>
<header class="site-header">
  <div class="brand"><span class="brand-dot"></span>Saltmere</div>
  <nav class="main-nav">
    <span>Home</span><span>Where to Stay</span><span>Caravan and Camping</span><span>Bed and Breakfast</span><span class="active">Hotels</span><span>Contact Us</span>
  </nav>
</header>

<section class="page-hero">
  <h1>Hotels</h1>
  <p class="breadcrumb">Home / Hotels</p>
</section>

<main class="listing">
  <h2>Hotels in Dorrin</h2>
  <p class="intro">Most visitors to Dorrin stay at one of its hotels, each within easy reach of the harbour and beaches. All information on this page is listed as of March 2018. To make a booking enquiry, please contact the hotels directly.</p>

  <div class="card-grid">
    <article class="card">
      <div class="card-photo" role="img" aria-label="Photo of Harbourview Hotel seafront facade" style="background:linear-gradient(#c9d4da,#8e9aa2)"></div>
      <div class="card-body"><h3>Harbourview Hotel</h3>
        <p class="detail"><svg viewBox="0 0 10 10"><path d="M2 1h2l1 2-1 1a6 6 0 0 0 2 2l1-1 2 1v2c0 1-1 1-1 1A8 8 0 0 1 1 2s0-1 1-1z"/></svg><b>Telephone Number:</b> 01000 000101</p>
        <p class="detail"><svg viewBox="0 0 10 10"><path d="M1 2h8v6H1z M1 2l4 3 4-3" fill="none" stroke="#0aa3e0"/></svg><b>Email:</b> stay@harbourview.example</p>
        <p class="detail"><svg viewBox="0 0 10 10"><circle cx="5" cy="5" r="4" fill="none" stroke="#0aa3e0"/></svg><b>Website:</b> www.harbourview.example</p>
      </div>
    </article>
    <article class="card">
      <div class="card-photo" role="img" aria-label="Photo of The Glebe Hotel with garden" style="background:linear-gradient(#bcd0e0,#a7a58a)"></div>
      <div class="card-body"><h3>The Glebe Hotel</h3>
        <p class="detail"><svg viewBox="0 0 10 10"><path d="M2 1h2l1 2-1 1a6 6 0 0 0 2 2l1-1 2 1v2c0 1-1 1-1 1A8 8 0 0 1 1 2s0-1 1-1z"/></svg><b>Telephone Number:</b> 01000 000202</p>
        <p class="detail"><svg viewBox="0 0 10 10"><path d="M1 2h8v6H1z M1 2l4 3 4-3" fill="none" stroke="#0aa3e0"/></svg><b>Email:</b> info@glebehotel.example</p>
        <p class="detail"><svg viewBox="0 0 10 10"><circle cx="5" cy="5" r="4" fill="none" stroke="#0aa3e0"/></svg><b>Website:</b> www.glebehotel.example</p>
      </div>
    </article>
    <article class="card">
      <div class="card-photo" role="img" aria-label="Photo of The Westcliff Hotel terrace frontage" style="background:linear-gradient(#d4dde4,#b8b3aa)"></div>
      <div class="card-body"><h3>The Westcliff Hotel</h3>
        <p class="detail"><svg viewBox="0 0 10 10"><path d="M2 1h2l1 2-1 1a6 6 0 0 0 2 2l1-1 2 1v2c0 1-1 1-1 1A8 8 0 0 1 1 2s0-1 1-1z"/></svg><b>Telephone Number:</b> 01000 000303</p>
        <p class="detail"><svg viewBox="0 0 10 10"><circle cx="5" cy="5" r="4" fill="none" stroke="#0aa3e0"/></svg><b>Website:</b> www.westcliff.example</p>
      </div>
    </article>
    <article class="card">
      <div class="card-photo" role="img" aria-label="Photo of Ashcombe House Hotel white facade" style="background:linear-gradient(#c6d2da,#9fa39e)"></div>
      <div class="card-body"><h3>Ashcombe House Hotel</h3>
        <p class="detail"><svg viewBox="0 0 10 10"><path d="M2 1h2l1 2-1 1a6 6 0 0 0 2 2l1-1 2 1v2c0 1-1 1-1 1A8 8 0 0 1 1 2s0-1 1-1z"/></svg><b>Telephone Number:</b> 01000 000404</p>
        <p class="detail"><svg viewBox="0 0 10 10"><path d="M1 2h8v6H1z M1 2l4 3 4-3" fill="none" stroke="#0aa3e0"/></svg><b>Email:</b> info@ashcombehouse.example</p>
        <p class="detail"><svg viewBox="0 0 10 10"><circle cx="5" cy="5" r="4" fill="none" stroke="#0aa3e0"/></svg><b>Website:</b> www.ashcombehouse.example</p>
      </div>
    </article>
    <article class="card">
      <div class="card-photo" role="img" aria-label="Photo of The Glebe Hotel street view" style="background:linear-gradient(#8fb4d8,#9a948c)"></div>
      <div class="card-body"><h3>The Glebe Hotel</h3>
        <p class="detail"><svg viewBox="0 0 10 10"><path d="M2 1h2l1 2-1 1a6 6 0 0 0 2 2l1-1 2 1v2c0 1-1 1-1 1A8 8 0 0 1 1 2s0-1 1-1z"/></svg><b>Telephone Number:</b> 01000 000202</p>
        <p class="detail"><svg viewBox="0 0 10 10"><path d="M1 2h8v6H1z M1 2l4 3 4-3" fill="none" stroke="#0aa3e0"/></svg><b>Email:</b> info@glebehotel.example</p>
        <p class="detail"><svg viewBox="0 0 10 10"><circle cx="5" cy="5" r="4" fill="none" stroke="#0aa3e0"/></svg><b>Website:</b> www.glebehotel.example</p>
      </div>
    </article>
    <article class="card">
      <div class="card-photo" role="img" aria-label="Photo of The Westcliff Hotel yellow terrace" style="background:linear-gradient(#9cc3e6,#d8c98a)"></div>
      <div class="card-body"><h3>The Westcliff Hotel</h3>
        <p class="detail"><svg viewBox="0 0 10 10"><path d="M2 1h2l1 2-1 1a6 6 0 0 0 2 2l1-1 2 1v2c0 1-1 1-1 1A8 8 0 0 1 1 2s0-1 1-1z"/></svg><b>Telephone Number:</b> 01000 000303</p>
        <p class="detail"><svg viewBox="0 0 10 10"><path d="M1 2h8v6H1z M1 2l4 3 4-3" fill="none" stroke="#0aa3e0"/></svg><b>Email:</b> desk@westcliff.example</p>
        <p class="detail"><svg viewBox="0 0 10 10"><circle cx="5" cy="5" r="4" fill="none" stroke="#0aa3e0"/></svg><b>Website:</b> www.westcliff.example</p>
      </div>
    </article>
  </div>
  <span class="load-more">Load More</span>
</main>

<footer class="site-footer" role="img" aria-label="Footer with faint harbour photo backdrop">
  <div class="footer-brand"><div class="mark"></div><span>Saltmere</span></div>
  <div class="footer-col">
    <h4>Useful Links</h4>
    <ul><li>Home</li><li>Where to Stay</li><li>Caravan and Camping</li><li>Bed and Breakfast</li><li>Hotels</li><li>Contact Us</li></ul>
  </div>
  <div class="footer-col">
    <h4>Updates</h4>
    <div class="updates">
      <p class="feed-title">Posts by @DorrinTown</p>
      <div class="tweet"><span class="avatar"></span><p>Dorrin Town @DorrinTown<br>Sunny day on the north beach today, come and visit us.</p></div>
      <div class="tweet"><span class="avatar"></span><p>Dorrin Town @DorrinTown<br>New walking trails along the harbour open this weekend.</p></div>
    </div>
  </div>
</footer>
<div class="copyright"><strong>Saltmere</strong><span>Copyright © 2017 | All Right Reserved</span></div>
<div class="to-top"><svg width="8" height="8" viewBox="0 0 10 10"><path d="M1 7l4-4 4 4" fill="none" stroke="#fff" stroke-width="2"/></svg></div>
</body>
</html>
```